Flyer-Design für tamilisches Restaurant
Zielgruppe
Tamilisches Essen (kottu Rotti)
Aufgabenstellung
brauche eine zwei seitige A5 Flyer hoch oder quer spielt keine rolle das Hintergrund sollte Schwarz sein und paar Details in Gold wie unser Logo, das ist unsere Gedanke an design.
Auf der Vorderseite sollte, Neueröffnung am 01. März 2019 unser Hauptlogo, Facebook/ Instagram Logo in Gold mit unserer Seite (Selvo_Restaurant) und unser Motto #allaboutthebowl sein.
Auf der Rückseite, ein Bild mit kurzem Beschrieb ( Kottu Rotti das populärstes Gericht aus SriLanka)
Alle Gerichte zum mitnehmen und ab 8. März 2019 mit Lieferung.
unsere Öffnungszeiten
Montag bis Donnerstag 17.00 – 23.00 Uhr
Freitag 17.00 – 02.00 Uhr
Samstag 17.00 – 02.00 Uhr
Sonntag 17.00 – 23.00 Uhr
das Team von der Selvo freut such auf Ihren Besuch
Reservierungen unter 031 574 19 86
und noch unser Logo in klein Format

```html
<!DOCTYPE html>
<html lang="de">
<head>
<meta charset="utf-8">
<title>Selvo Flyer – Vorder- und Rückseite</title>
<link rel="stylesheet" href="https://fonts.googleapis.com/css2?family=Bebas+Neue&family=Montserrat:wght@800;900&family=Roboto+Slab:wght@400;700&family=Dancing+Script:wght@600&display=swap">
<style>
  :root {
    --bg: #2a2a2b;
    --black: #0b0b0b;
    --black-soft: #1b1b1b;
    --gold: #d9c07a;
    --gold-light: #f1e2a8;
    --gold-dark: #a88a45;
    --red: #7c1f1b;
    --paper: #e2cf97;
    --white: #ffffff;
  }
  * { box-sizing: border-box; margin: 0; padding: 0; }
  html, body { width: 1200px; height: 776px; overflow: hidden; }
  body { background: var(--bg); position: relative; font-family: "Roboto Slab", serif; }

  .flyer {
    position: absolute; top: 48px; width: 480px; height: 680px; overflow: hidden;
    background: radial-gradient(ellipse at 50% 35%, var(--black-soft), var(--black) 75%);
    box-shadow: 0 10px 30px rgba(0,0,0,.5);
  }
  .flyer--front { left: 100px; }
  .flyer--back { left: 620px; }
  .abs { position: absolute; }
  .center { left: 0; right: 0; text-align: center; }
  .gold-text {
    background: linear-gradient(180deg, var(--gold-light), var(--gold) 55%, var(--gold-dark));
    -webkit-background-clip: text; background-clip: text; color: transparent;
  }
  .band { position: absolute; left: 0; top: 0; }

  /* front */
  .headline { top: 26px; font-family: "Bebas Neue", sans-serif; font-size: 100px; line-height: 1; letter-spacing: 1px; }
  .date { top: 126px; font-family: "Montserrat", sans-serif; font-weight: 900; font-size: 30px; line-height: 1.1; color: var(--white); letter-spacing: 1px; }
  .tagline { top: 180px; font-family: "Montserrat", sans-serif; font-weight: 800; font-size: 14px; letter-spacing: 4px; color: var(--gold); }
  .brand-ring { left: 145px; top: 212px; width: 190px; height: 190px; border: 2px solid var(--gold); border-radius: 50%;
    display: flex; flex-direction: column; align-items: center; justify-content: center; }
  .brand-name { font-family: "Roboto Slab", serif; font-weight: 700; font-size: 44px; line-height: 1.1; color: var(--gold); letter-spacing: 2px; }
  .brand-est { font-family: "Montserrat", sans-serif; font-weight: 800; font-size: 13px; color: var(--gold); letter-spacing: 3px; margin-top: 4px; }
  .leaves { width: 80px; height: 100px; border-radius: 40% 60% 40% 60%;
    background: linear-gradient(135deg, var(--gold-light), var(--gold-dark)); opacity: .8; }
  .leaves--left { left: 6px; top: 405px; }
  .leaves--right { right: 6px; top: 400px; }
  .hours { left: 150px; top: 440px; width: 180px; height: 125px; background: var(--paper); padding: 10px 10px 0; }
  .hours__title { font-size: 12px; line-height: 1.3; font-weight: 700; color: var(--red); text-align: center; margin-bottom: 6px; }
  .hours__table { width: 100%; border-collapse: collapse; font-size: 8px; font-weight: 700; color: var(--black); }
  .hours__table td { padding: 0; line-height: 11px; white-space: nowrap; }
  .hours__table td:last-child { text-align: right; }
  .contact { left: 40px; top: 598px; color: var(--white); }
  .contact__label { font-size: 13px; line-height: 1.3; }
  .contact__tel { font-size: 24px; font-weight: 700; line-height: 1.15; white-space: nowrap; }
  .contact__addr { font-size: 10px; line-height: 1.4; font-weight: 700; white-space: nowrap; }
  .social { left: 318px; top: 612px; display: flex; align-items: center; gap: 10px; }
  .social__mark { width: 28px; height: 28px; background: var(--gold); flex: none; }
  .social__text { font-size: 12px; line-height: 1.35; color: var(--white); white-space: nowrap; }
  .social__tag { color: var(--gold); }

  /* back */
  .dish-title { top: 22px; font-family: "Bebas Neue", sans-serif; font-size: 110px; line-height: 1; letter-spacing: 1px; }
  .photo-frame { left: 40px; top: 140px; width: 400px; height: 235px; border: 3px solid var(--red); }
  .photo { width: 100%; height: 100%;
    background: radial-gradient(ellipse at 50% 62%, #c25a24 0 22%, #f2f0ec 23% 40%, #0d0d0d 41%); }
  .ribbon-top { left: 150px; top: 126px; width: 180px; height: 22px; background: var(--red);
    font-family: "Dancing Script", cursive; font-size: 15px; color: var(--gold); text-align: center; line-height: 22px; }
  .stars { top: 150px; font-size: 11px; color: var(--gold); letter-spacing: 2px; }
  .ribbon-claim { left: 20px; top: 366px; width: 440px; height: 32px; background: var(--red);
    font-weight: 700; font-size: 13px; letter-spacing: 1.5px; color: var(--gold); text-align: center; line-height: 32px; white-space: nowrap; }
  .reserve { left: 40px; top: 418px; display: flex; align-items: center; gap: 8px; color: var(--white); }
  .reserve__label { font-size: 10px; line-height: 1.3; }
  .reserve__tel { font-family: "Bebas Neue", sans-serif; font-size: 30px; line-height: 1; white-space: nowrap; }
  .divider { left: 226px; top: 416px; width: 2px; height: 50px; background: var(--gold); }
  .delivery { left: 242px; top: 424px; width: 210px; font-size: 11.5px; line-height: 1.6; color: var(--white); white-space: nowrap; }
  .mini-brand { left: 210px; top: 495px; width: 60px; height: 60px; border-radius: 50%; background: var(--black);
    border: 2px solid var(--gold); display: flex; align-items: center; justify-content: center;
    font-size: 11px; font-weight: 700; color: var(--gold); letter-spacing: 1px; }
  .team { top: 605px; font-size: 12px; line-height: 1.3; color: var(--gold); }
</style>
</head>
<body>

<section class="flyer flyer--front" aria-label="Vorderseite">
  <h1 class="abs center headline gold-text">NEUERÖFFNUNG</h1>
  <p class="abs center date">AM 01. MÄRZ 2019</p>
  <p class="abs center tagline">RESTAURANT · BAR · CATERING</p>
  <div class="abs brand-ring">
    <span class="brand-name">SELVO</span>
    <span class="brand-est">EST. 2019</span>
  </div>
  <div class="abs leaves leaves--left" role="img" aria-label="Goldene Blattzweige"></div>
  <div class="abs leaves leaves--right" role="img" aria-label="Goldene Blattzweige"></div>

  <svg class="band" width="480" height="680" viewBox="0 0 480 680" aria-hidden="true">
    <path d="M0 555 Q240 605 480 515 L480 680 L0 680 Z" fill="var(--red)"/>
    <path d="M0 555 Q240 605 480 515" fill="none" stroke="var(--gold)" stroke-width="4"/>
  </svg>

  <div class="abs hours">
    <h2 class="hours__title">Unsere Öffnungszeiten</h2>
    <table class="hours__table">
      <tr><td>Montag:</td><td>17.00 Uhr – 23.00 Uhr</td></tr>
      <tr><td>Dienstag:</td><td>17.00 Uhr – 23.00 Uhr</td></tr>
      <tr><td>Mittwoch:</td><td>17.00 Uhr – 23.00 Uhr</td></tr>
      <tr><td>Donnerstag:</td><td>17.00 Uhr – 23.00 Uhr</td></tr>
      <tr><td>Freitag:</td><td>17.00 Uhr – 02.00 Uhr</td></tr>
      <tr><td>Samstag:</td><td>17.00 Uhr – 02.00 Uhr</td></tr>
      <tr><td>Sonntag:</td><td>17.00 Uhr – 23.00 Uhr</td></tr>
    </table>
  </div>

  <div class="abs contact">
    <p class="contact__label">Reservierungen unter</p>
    <p class="contact__tel gold-text">Tel.: 031 574 19 86</p>
    <p class="contact__addr">Lindenweggasse 7 | 4550 Solmatt</p>
  </div>
  <div class="abs social">
    <span class="social__mark"></span>
    <p class="social__text">Selvo_Restaurant<br><span class="social__tag">#allaboutthebowl</span></p>
  </div>
</section>

<section class="flyer flyer--back" aria-label="Rückseite">
  <h2 class="abs center dish-title gold-text">KOTTU ROTTI</h2>
  <div class="abs photo-frame">
    <div class="photo" role="img" aria-label="Foto: Teller mit Kottu Rotti, Zitrone, Zwiebelringen und Petersilie"></div>
  </div>
  <p class="abs ribbon-top">Mmmh...lecker</p>
  <p class="abs center stars">★★★★★</p>
  <p class="abs ribbon-claim">DAS POPULÄRSTES GERICHT AUS SRILANKA</p>

  <div class="abs reserve">
    <svg width="24" height="24" viewBox="0 0 24 24" aria-hidden="true">
      <circle cx="12" cy="12" r="11" fill="none" stroke="var(--white)" stroke-width="1.5"/>
      <path d="M8 6.5c-1 .8-1.2 2.3-.4 3.9 1.3 2.6 3.4 4.7 6 6 1.6.8 3.1.6 3.9-.4l-2-2-1.5.9c-1.2-.6-2.6-2-3.2-3.2l.9-1.5z" fill="var(--white)"/>
    </svg>
    <div>
      <p class="reserve__label">Reservierungen unter:</p>
      <p class="reserve__tel gold-text">031 574 19 86</p>
    </div>
  </div>
  <span class="abs divider"></span>
  <p class="abs delivery">Alle Gerichte zum mitnehmen<br>und ab 8. März 2019 mit Lieferung.</p>

  <svg class="band" width="480" height="680" viewBox="0 0 480 680" aria-hidden="true">
    <path d="M0 505 Q240 560 480 470 L480 680 L0 680 Z" fill="var(--red)"/>
    <path d="M0 505 Q240 560 480 470" fill="none" stroke="var(--gold)" stroke-width="4"/>
    <line x1="180" y1="637" x2="300" y2="637" stroke="var(--gold)" stroke-width="1"/>
    <rect x="172" y="633" width="8" height="8" transform="rotate(45 176 637)" fill="var(--gold)"/>
    <rect x="300" y="633" width="8" height="8" transform="rotate(45 304 637)" fill="var(--gold)"/>
  </svg>

  <div class="abs mini-brand">SELVO</div>
  <p class="abs center team">Das Team von der Selvo freut sich auf Ihren Besuch.</p>
</section>

</body>
</html>
```